Brick pressure cleaning business needs business cards that are memorable

The business is called Foremost jetstream brick and pressure cleaning.
we blast bricks on new houses and driveways. I would like a logo with water spraying out of the letter s in the wording. Also bricks on the card somehow and maybe the word foremost to be on an angle above the rest of the business name if possible. some shinny gold would be nice somewhere to. Would like to list our services on the back of card- red and cream brick clean, green stain removal, floor scrapes, fence panel clean or changeout. Driveway cleans. hard surface pressure cleans.

Target Market(s)

Building companies and home reno people

Industry/Entity Type

construction

Contact Information for Business Card

business name,phone,number my name, services on the back

Colors
0054AA
0677BA
7BADD7
CADEEF
E8F1F8
FFF300
FFF600
FEFA6F
FFFEC7
FFFEE8

```html
<!DOCTYPE html>
<html lang="en">
<head>
<meta charset="utf-8">
<title>Foremost Jetstream – Business Card</title>
<link href="https://fonts.googleapis.com/css2?family=Poppins:wght@300;400;500;600&display=swap" rel="stylesheet">
<style>
  :root {
    --blue: #0a4da2;
    --sky: #1a8ad4;
    --orange: #f7941d;
    --paper: #ffffff;
    --backdrop: #e4e5e6;
  }
  * { margin: 0; padding: 0; box-sizing: border-box; }
  html, body { width: 1200px; height: 900px; overflow: hidden; }
  body {
    position: relative;
    background: var(--backdrop);
    font-family: "Poppins", sans-serif;
    color: var(--blue);
  }
  .card {
    position: absolute;
    top: 216px;
    width: 309px;
    height: 501px;
    background: var(--paper);
  }
  .card--back { left: 279px; border-radius: 0 62px 0 62px; }
  .card--front { left: 617px; border-radius: 62px 0 62px 0; }

  .brand { position: absolute; display: flex; align-items: center; gap: 12px; }
  .card--back .brand { left: 52px; top: 104px; }
  .card--front .brand { left: 45px; top: 113px; }
  .brand__square {
    width: 65px; height: 65px;
    border: 2px solid var(--blue);
    flex: none;
  }
  .card--front .brand__square { width: 69px; height: 69px; }
  .brand__name {
    font-weight: 500;
    color: var(--blue);
    line-height: 1.15;
  }
  .brand__main { display: block; font-size: 22px; letter-spacing: 0.5px; line-height: 1.05; }
  .brand__sub { display: block; font-size: 8.6px; letter-spacing: 0.9px; text-transform: uppercase; }

  .services {
    position: absolute;
    left: 22px;
    top: 306px;
    list-style: none;
    font-size: 15px;
    font-weight: 400;
    line-height: 18px;
  }
  .services li { position: relative; padding-left: 22px; }
  .services li::before {
    content: "";
    position: absolute;
    left: 0; top: 7px;
    width: 10px; height: 5px;
    background: var(--orange);
  }

  .person { position: absolute; left: 32px; top: 296px; }
  .person__name { font-size: 19px; font-weight: 600; line-height: 22px; letter-spacing: 0.2px; }
  .person__role { font-size: 14px; font-weight: 400; color: var(--orange); line-height: 16px; }

  .contacts {
    position: absolute;
    left: 32px; top: 349px;
    list-style: none;
    font-size: 14.5px;
    line-height: 18px;
  }
  .contacts li { display: flex; align-items: center; gap: 5px; }
  .contacts svg { width: 13px; height: 13px; flex: none; }

  .address {
    position: absolute;
    left: 33px; top: 417px;
    font-size: 14.5px;
    line-height: 18px;
    font-style: normal;
  }
</style>
</head>
<body>

<section class="card card--back">
  <div class="brand">
    <div class="brand__square"></div>
    <div class="brand__name">
      <span class="brand__main">FOREMOST</span>
      <span class="brand__sub">Jetstream brick and</span>
      <span class="brand__sub">pressure cleaning</span>
    </div>
  </div>
  <ul class="services">
    <li>Red and cream brick clean</li>
    <li>Green stain removal</li>
    <li>Floor scrapes</li>
    <li>Fence panel clean or changeout</li>
    <li>Driveway cleans</li>
    <li>Hard surface pressure cleans</li>
  </ul>
</section>

<section class="card card--front">
  <div class="brand">
    <div class="brand__square"></div>
    <div class="brand__name">
      <span class="brand__main">FOREMOST</span>
      <span class="brand__sub">Jetstream brick and</span>
      <span class="brand__sub">pressure cleaning</span>
    </div>
  </div>

  <div class="person">
    <p class="person__name">DANIEL HARTLEY</p>
    <p class="person__role">Managing Director</p>
  </div>

  <ul class="contacts">
    <li>
      <svg viewBox="0 0 24 24" aria-hidden="true"><path fill="none" stroke="#f7941d" stroke-width="2.4" stroke-linecap="round" d="M6 3l3 4-2 2.5a12 12 0 0 0 7.5 7.5L17 15l4 3-2 3C10 21 3 14 3 5z M14 3a7 7 0 0 1 7 7 M14 7a3 3 0 0 1 3 3"/></svg>
      044-987 654 321
    </li>
    <li>
      <svg viewBox="0 0 24 24" aria-hidden="true"><rect x="1" y="4" width="22" height="16" fill="#f7941d"/><path d="M1 4l11 9 11-9" fill="none" stroke="#fff" stroke-width="2"/></svg>
      hello@foremostjet.com
    </li>
    <li>
      <svg viewBox="0 0 24 24" aria-hidden="true"><g fill="none" stroke="#f7941d" stroke-width="2"><circle cx="12" cy="12" r="10"/><ellipse cx="12" cy="12" rx="4.5" ry="10"/><path d="M2 12h20M4 7h16M4 17h16"/></g></svg>
      www.foremostjet.com
    </li>
  </ul>

  <address class="address">
    17 Quarry Lane, Brickfield<br>
    3810, Country Name
  </address>
</section>

</body>
</html>
```